Need posters that inspire entrepreneurs

I want to create beautiful, inspiring wall art. I'm looking for a designer to create an awesome sample (note this sample is not for real use). The winning design will form the foundation of our art "style" so there will be LOTS of ongoing work for the winning designer.

It's your challenge to create a style that is clean, inspiring and timeless, and possibly can be adapted to different colour palettes.

Looking for a perfect execution of words, image and design.

The attached example shows one idea. It should serve as an idea only.

Format of the images should be either rectangular or square. Exact size is preferably UK A4 (US letter) or max A3. Assume that a display would consist of a 4 x 4 image grid so size needs to allow for that in a small to medium size office.

The quotes I want in the 3 samples (each in an individual poster - not combined in 1 poster). Each quote should have it's own, the reason for three is to prove the design work on more than one quote. The quotes are:

1) Failure is the condiment that gives success its flavor.
– Wendell Ruskin

2) Whether you think you can or think you can’t, you’re right.
– Milo Dagwell

3) Ever tried. Ever failed. No matter. Try Again. Fail again. Fail better.
– Oswin Tarrant

Each design should include the image of the person and the quote + any design elements you consider relevant. You should find relevant images of the individuals being quoted. The final images will not be published or used commercially in any way.

Font styles to use
Serif
Sans Serif

Colors

Designer to choose colors to be used in the design.

Requirements
Must have
• Words and headshot image - 1 per poster design.
• Please consider in the design that there will not always be photographs of the person quoted and as such the design will need to hold, whether the source is a photo, sketch or something else.
Nice to have
• None, but note that the final image will be printed on a wall mounted board, printed to the edge but not on the edge. The board will have black or white edges so consider in the design.
Should not have
• None

```html
<!DOCTYPE html>
<html lang="en">
<head>
<meta charset="utf-8">
<title>Quote Poster — Milo Dagwell</title>
<link rel="stylesheet" href="https://fonts.googleapis.com/css2?family=Libre+Caslon+Text&display=swap">
<style>
  :root {
    --ink-black: #000000;
    --deep-navy: #0a1a3e;
    --royal-navy: #0c2a6e;
    --paper-white: #ffffff;
    --portrait-light: #8a8a8a;
    --portrait-dark: #141414;
  }
  html, body {
    margin: 0;
    padding: 0;
    width: 1200px;
    height: 1200px;
    overflow: hidden;
  }
  .poster {
    position: relative;
    width: 1200px;
    height: 1200px;
    background: linear-gradient(90deg, var(--ink-black) 0%, var(--ink-black) 38%, var(--deep-navy) 68%, var(--royal-navy) 100%);
    font-family: "Libre Caslon Text", Georgia, serif;
    color: var(--paper-white);
  }
  .portrait {
    position: absolute;
    left: 0;
    top: 55px;
    width: 340px;
    height: 1145px;
    background:
      radial-gradient(ellipse 80% 55% at 20% 45%, var(--portrait-light) 0%, #4a4a4a 45%, var(--portrait-dark) 80%, transparent 100%);
  }
  .quote {
    position: absolute;
    right: 135px;
    top: 268px;
    margin: 0;
    text-align: right;
    font-size: 86px;
    line-height: 114px;
    font-weight: 400;
    letter-spacing: -1px;
    text-shadow: 0 3px 6px rgba(0, 0, 0, 0.55);
  }
  .quote .line { display: block; }
  .attribution {
    position: absolute;
    right: 115px;
    top: 1010px;
    margin: 0;
    font-size: 30px;
    text-shadow: 0 2px 4px rgba(0, 0, 0, 0.5);
  }
</style>
</head>
<body>
  <main class="poster">
    <div class="portrait" role="img" aria-label="Black and white headshot portrait of Milo Dagwell, cropped at the left edge"></div>
    <blockquote class="quote">
      <span class="line">Whether</span>
      <span class="line">you think</span>
      <span class="line">you can</span>
      <span class="line">or think</span>
      <span class="line">you can’t,</span>
      <span class="line">you’re right.</span>
    </blockquote>
    <p class="attribution">Milo Dagwell</p>
  </main>
</body>
</html>
```